Web Design for an Online Dating Web Site

We need an uncoded web design for a new online dating web site called zMatchy.net. Simplicity and boldness are the key factors in the successful design.
Please look at the requirements document attached for details.
Updates
Dear all,
Please AVOID USING A PICTURE OF A HAPPY COUPLE ON THE HOME PAGE of the site. We highly want to move away from this space as it makes our web site just like another dating web site.
We like something simple with web 2.0 look and feel. The examples in the Requirements Document are exactly the design we are after.
Regards
Tarn
Industry/Entity Type
Dating
Look and feel
Each slider illustrates characteristics of the customer's brand and the style your logo design should communicate.

```html
<!DOCTYPE html>
<html lang="en">
<head>
<meta charset="utf-8">
<title>zMatchy.net – My Messages</title>
<link rel="stylesheet" href="https://fonts.googleapis.com/css2?family=Arimo:wght@400;700&family=Open+Sans:wght@400;600&display=swap">
<style>
:root{
  --pink:#ec5f98;
  --pink-dark:#d9437f;
  --grey-btn-dark:#a5a5a5;
  --blue-tab:#7ab9e6;
  --blue-top:#aad9f6;
  --blue-bottom:#7ebde8;
  --link-blue:#6aaed6;
  --name-blue:#8ec3df;
  --text:#555;
  --line:#e2e2e2;
  --footer:#1c1c1c;
  --footer-head:#111;
  --footer-text:#6e6e6e;
  --field:#3a3a3a;
  --white:#fff;
}
*{box-sizing:border-box;margin:0;padding:0}
html,body{width:1046px;height:1200px;overflow:hidden;background:var(--white)}
body{font-family:"Arimo",Arial,sans-serif;color:var(--text)}
.page{position:relative;width:994px;height:1140px;transform:scale(1.0523,1.0526);transform-origin:0 0}
.abs{position:absolute}

/* header */
.header{left:0;top:0;width:994px;height:186px;background:var(--white);border-bottom:3px solid #ddd}
.brand{left:68px;top:30px;display:flex;align-items:center;gap:10px}
.brand-dot{width:22px;height:22px;border-radius:50%;background:var(--pink)}
.brand-name{font-family:"Arimo",sans-serif;font-weight:700;font-size:56px;color:#6b6b6b;letter-spacing:-1px}
.nav-btn{top:40px;height:31px;border-radius:10px;color:#fff;font-size:16px;line-height:31px;text-align:center;
  background:linear-gradient(#cfcfcf,var(--grey-btn-dark));text-shadow:0 1px 0 rgba(0,0,0,.15)}
.nav-btn.active{background:linear-gradient(#f57aa9,var(--pink-dark))}
.stuff-tab{left:505px;top:80px;width:104px;height:32px;background:var(--blue-tab);border-radius:10px 10px 0 0;color:#fff;font-size:15px;line-height:32px;padding-left:13px}
.stuff-tab .caret{position:absolute;right:0;top:0;width:26px;height:32px;border-left:1px solid #a8d3f0}
.stuff-tab .caret:after{content:"";position:absolute;left:8px;top:13px;border:5px solid transparent;border-top:7px solid #fff}
.stuff-panel{left:505px;top:110px;width:320px;height:57px;background:var(--blue-tab);border-radius:0 12px 14px 14px}
.stuff-item{position:absolute;color:#fff;font-size:11px;display:flex;align-items:center;gap:5px;white-space:nowrap}
.stuff-item i{display:inline-block;width:15px;height:13px;background:#e8f1f7;border-radius:2px}

/* body band */
.band{left:0;top:189px;width:994px;height:646px;background:linear-gradient(var(--blue-top),var(--blue-bottom))}
.card{left:78px;top:228px;width:836px;height:530px;background:var(--white);border-radius:12px;box-shadow:0 0 4px rgba(0,0,0,.12);overflow:hidden}
.inbox{left:0;top:0;width:276px;height:530px;border-right:1px solid var(--line)}
.inbox h2{position:absolute;left:34px;top:12px;font-weight:400;font-size:18px;color:#555}
.msg{position:absolute;left:0;width:275px;height:97px;border-bottom:1px solid #eee;background:linear-gradient(#fdfdfd,#f6f6f6)}
.msg.current{background:linear-gradient(#e7f4fc,#d4ebf8)}
.avatar{position:absolute;left:14px;top:10px;width:66px;height:66px;border:3px solid #fff;box-shadow:0 0 3px rgba(0,0,0,.3);border-radius:2px}
.avatar.photo{background:linear-gradient(135deg,#7e9a45,#a33c6e 55%,#6d6f5a)}
.avatar.photo2{background:linear-gradient(135deg,#3f3733,#a28472 55%,#5b4a44)}
.avatar.plain{background:linear-gradient(#f3f3f3,#d8d8d8)}
.who{position:absolute;left:0;width:94px;top:80px;text-align:center;font-family:"Open Sans",sans-serif;font-size:12px;color:#555}
.lbl{position:absolute;width:68px;left:94px;text-align:right;font-size:12px}
.lbl.subj{top:20px;color:#555}
.lbl.body{top:43px;color:var(--link-blue)}
.val{position:absolute;left:166px;width:106px;height:22px;line-height:22px;font-family:"Open Sans",sans-serif;font-size:13px;white-space:nowrap;overflow:hidden;text-overflow:ellipsis;border-bottom:1px solid #e6e6e6;padding-left:6px}
.val.subj{top:16px;color:#555}
.val.body{top:39px;color:var(--link-blue);border-bottom:none}
.date{position:absolute;left:94px;width:68px;top:66px;text-align:right;font-size:10px;letter-spacing:1px;color:var(--link-blue)}

.sender-photo{left:318px;top:18px;width:146px;height:134px;border:3px solid #fff;box-shadow:0 0 3px rgba(0,0,0,.3);background:linear-gradient(135deg,#6f8e3a,#a03a6a 55%,#6f6e5c)}
.sender-name{left:472px;top:60px;font-size:18px;color:var(--name-blue)}
.sender-date{left:472px;top:83px;font-size:10px;letter-spacing:1px;color:var(--link-blue)}
.field-label{left:318px;font-size:18px;color:#555}
.subject-box{left:318px;top:192px;width:478px;height:31px;border:1px solid #ddd;font-family:"Open Sans",sans-serif;font-size:13px;line-height:29px;padding-left:11px;color:#444}
.editor{left:318px;top:262px;width:478px;height:221px;border:1px solid #ddd}
.toolbar{height:32px;background:#ececec;display:flex;align-items:center;gap:8px;padding-left:22px}
.tb{height:21px;min-width:22px;border:1px solid #c9c9c9;border-radius:4px;background:linear-gradient(#fff,#e3e3e3);font-size:10px;line-height:19px;text-align:center;color:#333;padding:0 4px}
.tb.font{width:84px}
.tb b{font-size:12px}
.editor-area{padding:6px 11px;font-family:"Open Sans",sans-serif;font-size:13px;color:#666}
.send-btn{left:513px;top:490px;width:86px;height:30px;border-radius:10px;background:linear-gradient(#f57aa9,var(--pink-dark));color:#fff;font-size:15px;line-height:30px;text-align:center}

.pager{left:430px;top:772px;display:flex;align-items:center;gap:11px;font-size:13px;color:#fff}
.pager .on{font-weight:700}

/* footer */
.footer{left:0;top:835px;width:994px;height:305px;background:var(--footer)}
.footer-strip{left:0;top:835px;width:994px;height:30px;background:var(--footer-head)}
.foot-h{top:843px;color:#fff;font-size:13px}
.foot-links{left:136px;top:873px;font-size:11px;line-height:16px;color:var(--footer-text);list-style:none}
.foot-field{left:308px;width:124px;height:22px;background:var(--field);border-radius:4px;font-size:10px;color:#777;padding:5px 10px}
.foot-area{left:308px;top:936px;width:181px;height:114px;background:var(--field);border-radius:4px;font-size:10px;color:#777;padding:5px 10px}
.foot-send{left:308px;top:1056px;width:67px;height:22px;background:#2c2c2c;border-radius:3px;color:#fff;font-size:13px;line-height:22px;text-align:center}
.social{top:877px;width:22px;height:22px;border-radius:3px}
.count{left:583px;top:908px;width:38px;height:22px;background:#fff;border-radius:3px;font-size:11px;line-height:22px;text-align:center;color:#a2433c}
.like-box{left:540px;top:940px;width:46px;height:22px;background:#eef0f6;border:1px solid #c5cbd9;border-radius:3px}
.likes{left:594px;top:945px;font-size:10px;color:#777;display:flex;align-items:center;gap:5px}
.likes i{width:10px;height:10px;background:#3b5998}
.contact{left:736px;top:874px;font-size:10px;line-height:16px;color:var(--footer-text)}
.contact .phone{color:#cfcfcf}
.foot-brand{left:738px;top:925px;display:flex;align-items:center;gap:6px}
.foot-brand span{font-weight:700;font-size:30px;color:#8a8a8a}
.foot-brand i{width:12px;height:12px;border-radius:50%;background:#8a8a8a}
.copy{left:0;width:994px;top:1106px;text-align:center;font-size:9px;line-height:15px;color:#666}
</style>
</head>
<body>
<div class="page">

  <header class="abs header">
    <div class="abs brand"><span class="brand-dot"></span><span class="brand-name">zMatchy</span></div>
    <div class="abs nav-btn active" style="left:505px;width:122px">my messages</div>
    <div class="abs nav-btn" style="left:636px;width:102px">start dating</div>
    <div class="abs nav-btn" style="left:747px;width:86px">sign out</div>
    <div class="abs nav-btn" style="left:842px;width:61px">help</div>
    <div class="abs stuff-tab">my stuff<span class="caret"></span></div>
    <nav class="abs stuff-panel">
      <span class="stuff-item" style="left:13px;top:10px"><i></i>My Details</span>
      <span class="stuff-item" style="left:104px;top:10px"><i></i>My Friends</span>
      <span class="stuff-item" style="left:191px;top:10px"><i></i>My Seeking Criteria</span>
      <span class="stuff-item" style="left:10px;top:30px"><i></i>My Avatar</span>
      <span class="stuff-item" style="left:100px;top:30px"><i></i>My Video</span>
    </nav>
  </header>

  <div class="abs band"></div>

  <main class="abs card">
    <section class="abs inbox">
      <h2>My Messages</h2>
      <div class="msg current" style="top:42px">
        <div class="avatar photo" role="img" aria-label="Member photo of Lena"></div>
        <div class="who">Lena</div>
        <div class="lbl subj">Subject:</div><div class="val subj">Whats up cutie? Let's Talk</div>
        <div class="lbl body">Message:</div><div class="val body">You should text me sometime</div>
        <div class="date">10/05/2011</div>
      </div>
      <div class="msg" style="top:139px">
        <div class="avatar photo2" role="img" aria-label="Member photo of Nichole"></div>
        <div class="who">Nichole</div>
        <div class="lbl subj">Subject:</div><div class="val subj">I'm new here and looking</div>
        <div class="lbl body">Message:</div><div class="val body">I want to set up a date</div>
        <div class="date">10/03/2011</div>
      </div>
      <div class="msg" style="top:236px">
        <div class="avatar plain" role="img" aria-label="Default female avatar"></div>
        <div class="who">Jessica</div>
        <div class="lbl subj">Subject:</div><div class="val subj">I'm new here and looking</div>
        <div class="lbl body">Message:</div><div class="val body">I want to set up a date</div>
        <div class="date">09/27/2011</div>
      </div>
      <div class="msg" style="top:333px">
        <div class="avatar plain" role="img" aria-label="Default male avatar"></div>
        <div class="who">Dallas</div>
        <div class="lbl subj">Subject:</div><div class="val subj">I'm new here and looking</div>
        <div class="lbl body">Message:</div><div class="val body">I want to set up a date</div>
        <div class="date">09/23/2011</div>
      </div>
      <div class="msg" style="top:430px">
        <div class="avatar photo" role="img" aria-label="Member photo of Lena"></div>
        <div class="who">Lena</div>
        <div class="lbl subj">Subject:</div><div class="val subj">I'm new here and looking</div>
        <div class="lbl body">Message:</div><div class="val body">I want to set up a date</div>
        <div class="date">09/15/2011</div>
      </div>
    </section>

    <div class="abs sender-photo" role="img" aria-label="Profile photo of Lena Brooks"></div>
    <div class="abs sender-name">Lena Brooks</div>
    <div class="abs sender-date">10/05/2011</div>
    <div class="abs field-label" style="top:169px">Subject</div>
    <div class="abs subject-box">RE: Whats up cutie? Let's Talk</div>
    <div class="abs field-label" style="top:235px">Enter Response</div>
    <div class="abs editor">
      <div class="toolbar">
        <span class="tb font">Verdana ▾</span>
        <span class="tb">12▾</span>
        <span class="tb"><b>B</b></span>
        <span class="tb"><i>I</i></span>
        <span class="tb"><u>U</u></span>
        <span class="tb"><s>ABC</s></span>
        <span class="tb">≡</span>
        <span class="tb">≡</span>
        <span class="tb">≡</span>
        <span class="tb">▦</span>
        <span class="tb">☺</span>
        <span class="tb">Σ</span>
      </div>
      <div class="editor-area">Enter response here...</div>
    </div>
    <div class="abs send-btn">send</div>
  </main>

  <nav class="abs pager">
    <svg width="20" height="16" viewBox="0 0 20 16"><path d="M0 8 9 0v5h11v6H9v5z" fill="#ec5f98"/></svg>
    <span class="on">1</span><span>2</span><span>3</span><span>4</span><span>5</span>
    <svg width="20" height="16" viewBox="0 0 20 16"><path d="M20 8 11 0v5H0v6h11v5z" fill="#3d9ad8"/></svg>
  </nav>

  <footer>
    <div class="abs footer"></div>
    <div class="abs footer-strip"></div>
    <div class="abs foot-h" style="left:137px">Read More</div>
    <div class="abs foot-h" style="left:311px">Let's Talk</div>
    <div class="abs foot-h" style="left:540px">Get Social</div>
    <div class="abs foot-h" style="left:737px">Contact Us</div>
    <ul class="abs foot-links">
      <li>Why zMatchy?</li><li>How It Works</li><li>Sign Up</li><li>Login</li><li>About Us</li>
    </ul>
    <div class="abs foot-field" style="top:876px">name</div>
    <div class="abs foot-field" style="top:906px">email address</div>
    <div class="abs foot-area">type message here...</div>
    <div class="abs foot-send">Send</div>
    <div class="abs social" style="left:540px;background:#3b5998"></div>
    <div class="abs social" style="left:570px;background:#f08a24"></div>
    <div class="abs social" style="left:600px;background:#3fa1d6"></div>
    <div class="abs social" style="left:630px;background:#2f7b3a"></div>
    <div class="abs social" style="left:540px;top:908px;width:36px;background:#e3e7ee"></div>
    <div class="abs count">1.4k</div>
    <div class="abs like-box"></div>
    <div class="abs likes"><i></i>3,400 Likes</div>
    <div class="abs contact">418 Sample Lane<br>60123, Ohio<br><span class="phone">1.800.SAMPLES</span></div>
    <div class="abs foot-brand"><i></i><span>zMatchy</span></div>
    <div class="abs copy">© 2011 zMatchy.net<br>zMatchy #1 Trusted Relationship Site - Know Your Match</div>
  </footer>

</div>
</body>
</html>
```